Investor Pitch Deck for Startup

We need a pitch deck to help us secure early funding for our new startup that will be active in the social media space. We have drafted out a 19 slide presentation, and have some other materials to help you prepare what we need.

We need to illustrate the pitch and make it visual, intuitive, and memorable. We are offering an abstract service, not a physical product - this might make it easier or harder to illustrate!

All materials will be provided after an NDA is signed.

Target Market(s)

This is aimed at angel investors.

Industry/Entity Type

Media

Font styles to use
Serif
Sans Serif

Requirements
Must have
• We are open to your suggestions about presentation and style.

```html
<!DOCTYPE html>
<html lang="en">
<head>
<meta charset="utf-8">
<title>KinThread – Investor Deck Overview</title>
<link href="https://fonts.googleapis.com/css2?family=Arimo:wght@400;700&display=swap" rel="stylesheet">
<style>
:root{
  --bg-top:#dcdee2;
  --bg:#b8bdc6;
  --teal-dark:#0d5a73;
  --teal:#1e8c7a;
  --green:#2e9e5b;
  --lime:#6aa332;
  --blue:#1a7fc6;
  --ink:#333;
  --muted:#8a8f96;
  --white:#fff;
}
*{box-sizing:border-box;margin:0;padding:0}
html,body{width:1200px;height:900px;overflow:hidden}
body{font-family:"Arimo",Arial,sans-serif;background:linear-gradient(var(--bg-top) 0 42px,#c9cdd3 42px,var(--bg) 900px);position:relative;color:var(--ink)}
.slide{position:absolute;width:244px;height:138px;background:var(--white);overflow:hidden;box-shadow:0 1px 3px rgba(0,0,0,.35)}
.num{position:absolute;font-size:7px;color:#555}
.abs{position:absolute}
.photo{position:absolute}
.dark{background:var(--teal-dark);color:var(--white)}
.h{font-weight:700;color:var(--green);font-size:9.5px;line-height:1.15}
.h-white{font-weight:700;color:var(--white);font-size:9.5px}
.body{font-size:4.3px;line-height:1.35}
.panel{position:absolute;background:var(--teal-dark);color:var(--white);padding:8px 6px}
.panel .title{color:#7ec3e0;font-weight:700;font-size:6.5px;margin-bottom:4px;line-height:1.1}
.brand{position:absolute;font-weight:700;color:var(--green)}
.brand-sm{position:absolute;right:6px;bottom:5px;font-size:5.5px;font-weight:700;color:var(--green);display:flex;align-items:center;gap:2px}
.brand-sm i{display:block;width:5px;height:5px;background:var(--blue)}
.box{position:absolute;color:var(--white);font-size:4.2px;line-height:1.3;padding:3px 4px;text-align:center}
.lbox{position:absolute;color:var(--white);font-size:4.4px;line-height:1.3;padding:4px}
.pie{position:absolute;width:26px;height:26px;border-radius:50%}
.pie-label{position:absolute;font-size:3px;color:#555;width:44px}
.bubble{position:absolute;border-radius:50%;color:#fff;font-size:3px;line-height:1.2;display:flex;align-items:center;justify-content:center;text-align:center;padding:3px}
table.fin{position:absolute;left:20px;top:30px;border-collapse:collapse;font-size:3.8px}
table.fin td,table.fin th{padding:1.6px 3px;text-align:left;width:70px}
table.fin th{background:var(--blue);color:#fff;font-weight:700}
table.fin tr:nth-child(odd) td:first-child{background:#c5e0a8}
table.fin tr:nth-child(even) td:first-child{background:#dcebc9}
table.fin tr:nth-child(odd) td{background:#e6e6e6}
table.fin tr:nth-child(even) td{background:#f2f2f2}
</style>
</head>
<body>

<!-- Row 1 -->
<div class="slide" style="left:25px;top:46px">
  <div class="brand" style="left:38px;top:40px;font-size:15px">KinThread</div>
  <div class="abs" style="left:50px;top:58px;font-size:4px;color:var(--blue)">KinThreadHub.com</div>
  <div class="abs" style="left:28px;top:100px;font-size:5px;color:var(--muted)">Sharing the Important Things in Life</div>
  <div class="panel" style="left:170px;top:0;width:74px;height:138px">
    <div class="abs" style="right:6px;bottom:12px;font-size:4.5px;text-align:right;line-height:1.4">Presenter<br>Date &amp; Location</div>
  </div>
</div>
<div class="num" style="left:25px;top:187px">1</div>

<div class="slide" style="left:325px;top:46px">
  <div class="photo" role="img" aria-label="Photo of railway tracks crossing at sunset" style="left:0;top:0;width:170px;height:138px;background:radial-gradient(circle at 45% 40%,#f0b060,#c0602a 55%,#6a2c12)"></div>
  <div class="panel" style="left:170px;top:0;width:74px;height:138px">
    <div class="title">We've all been there...</div>
    <div class="body">...an old friend passes away. A close friend, from years ago. We went her way and you went yours. Different adventures. Different parts of the world. New friends. New experiences.<br><br>And now she's gone. Tragic.<br><br>Sadder still – you're hearing about this now, and she died six months ago.</div>
  </div>
</div>
<div class="num" style="left:325px;top:187px">2</div>

<div class="slide" style="left:625px;top:46px">
  <div class="panel" style="left:0;top:0;width:66px;height:138px">
    <div class="title">We've all been there...</div>
    <div class="body">A close family member dies. You're helping arrange their funeral.<br><br>But you don't know who to invite. The family member has lived in different cities, and their friends and acquaintances have also moved around over the years.<br><br>Many people would want to know of the family member's passing and to share in remembering them.<br><br>But how to find them and tell them?</div>
  </div>
  <div class="photo" role="img" aria-label="Photo of a woman working at a laptop" style="left:66px;top:0;width:178px;height:138px;background:linear-gradient(120deg,#e9e4dc,#b89478 45%,#5b4638 70%,#d8d4cf)"></div>
</div>
<div class="num" style="left:625px;top:187px">3</div>

<div class="slide" style="left:925px;top:46px">
  <div class="photo" role="img" aria-label="Photo of two older men talking at a sports ground" style="left:0;top:0;width:168px;height:138px;background:linear-gradient(#9ec3e8 0 30%,#6d8a52 55%,#3a3f3a)"></div>
  <div class="panel" style="left:168px;top:0;width:76px;height:138px">
    <div class="title">We've all been there...</div>
    <div class="body">You and a friend are talking about a mutual acquaintance. Neither of you have heard from this person for a while.<br><br>Has something happened? Are they even still alive?<br><br>You don't like to raise the issue, and you both talk politely around this uncertainty, and have no easy way of resolving it, short of calling the person and saying "Are you still alive?"</div>
  </div>
</div>
<div class="num" style="left:925px;top:187px">4</div>

<!-- Row 2 -->
<div class="slide" style="left:25px;top:210px">
  <div class="photo" role="img" aria-label="Photo of a stack of newspapers" style="left:0;top:62px;width:110px;height:60px;background:linear-gradient(#f4f4f4,#bdbdbd 60%,#e8e8e8)"></div>
  <div class="h abs" style="left:100px;top:16px;width:134px;text-align:right">How Do We Announce or Hear About a Death?</div>
  <div class="body abs" style="left:128px;top:40px;width:106px;color:var(--muted);font-size:5px">We used to read newspaper death notices, but not any more, and anyway – most of us have moved away from our home towns.</div>
  <div class="brand-sm"><i></i>KinThread</div>
</div>
<div class="num" style="left:25px;top:351px">5</div>

<div class="slide" style="left:325px;top:210px">
  <div class="photo" role="img" aria-label="Photo of scattered social app tiles on a wooden table" style="left:0;top:0;width:244px;height:138px;background:linear-gradient(110deg,#c98a4a,#a8662e 45%,#6c8db0 70%,#c84a4a)"></div>
  <div class="abs h-white" style="left:19px;top:16px;line-height:1.1">How We<br>Communicate<br>Today</div>
  <ul class="abs" style="left:24px;top:53px;color:#fff;font-size:4.8px;line-height:1.55">
    <li>Last night's date</li><li>Favorite song</li><li>This morning's breakfast</li><li>Great photo</li><li>Terrific novel</li><li>Awesome video</li><li>Exciting new job</li><li>Amazing news</li>
  </ul>
</div>
<div class="num" style="left:325px;top:351px">6</div>

<div class="slide" style="left:625px;top:210px;background:#0b0b0b">
  <div class="abs" style="left:18px;top:30px;color:#a9a9a9;font-weight:700;font-size:15px;line-height:1.1">Solving a<br>Universal Need</div>
  <div class="abs body" style="left:18px;top:80px;width:128px;color:#fff;font-size:4.8px">Advising of and mourning a death, celebrating a life — regardless of distance, culture, demographics, KinThread addresses perennial needs in a new and engaging way.</div>
  <div class="photo" role="img" aria-label="Photo of a lit candle in darkness" style="left:150px;top:0;width:94px;height:138px;background:radial-gradient(ellipse at 50% 55%,#ffd27a 0,#c46a1a 12%,#2a1408 35%,#0b0b0b 60%)"></div>
</div>
<div class="num" style="left:625px;top:351px">7</div>

<div class="slide" style="left:925px;top:210px">
  <div class="brand" style="left:70px;top:60px;font-size:16px">KinThread</div>
  <div class="abs" style="left:100px;top:80px;font-size:4px;color:var(--blue)">KinThreadHub.com</div>
  <div class="abs" style="left:60px;top:107px;font-size:5px;color:var(--muted)">Sharing the Important Things in Life</div>
</div>
<div class="num" style="left:925px;top:351px">8</div>

<!-- Row 3 -->
<div class="slide" style="left:25px;top:374px">
  <div class="h abs" style="left:18px;top:16px">Universal Benefits</div>
  <div class="pie-label" style="left:16px;top:44px">Who contacts you about a death</div>
  <div class="pie" style="left:20px;top:56px;background:conic-gradient(#e03a2e 0 45%,#f2c12e 45% 60%,#2f7bd6 60% 80%,#9a9a9a 80%)"></div>
  <div class="pie-label" style="left:72px;top:44px">Missed funerals over five years</div>
  <div class="pie" style="left:76px;top:56px;background:conic-gradient(#2fa84f 0 40%,#e03a2e 40% 55%,#2f7bd6 55% 80%,#cfcfcf 80%)"></div>
  <div class="pie-label" style="left:128px;top:44px">Late news of a friend's passing</div>
  <div class="pie" style="left:132px;top:56px;background:conic-gradient(#f08a24 0 55%,#2f7bd6 55% 85%,#9a9a9a 85%)"></div>
  <div class="pie-label" style="left:184px;top:44px">Would use a shared alert service</div>
  <div class="pie" style="left:188px;top:56px;background:conic-gradient(#9a9a9a 0 60%,#2f7bd6 60% 85%,#d9d9d9 85%)"></div>
  <div class="brand-sm"><i></i>KinThread</div>
</div>
<div class="num" style="left:25px;top:515px">9</div>

<div class="slide" style="left:325px;top:374px">
  <div class="photo" role="img" aria-label="Illustration of one member figure linking to a growing crowd of figures" style="left:0;top:0;width:74px;height:138px;background:linear-gradient(#fff 0 45%,#dbe8f4 55%,#b8d3ea)"></div>
  <div class="panel" style="left:74px;top:0;width:170px;height:138px;padding:8px 12px">
    <div class="h-white" style="text-align:center;font-size:7.5px">True Viral Self-Growth Model</div>
    <div class="box" style="left:14px;top:28px;width:142px;background:var(--teal)">All members need to appoint at least two 'Linker' members (to report on their passing)</div>
    <div class="box" style="left:14px;top:50px;width:142px;background:var(--blue)">Research suggests average member will have 90+ people on their contact list</div>
    <div class="box" style="left:14px;top:72px;width:142px;background:var(--lime)">All contacts will be offered memberships<br>Research suggests high acceptance</div>
    <div class="box" style="left:14px;top:94px;width:142px;background:var(--blue)">Every new member gets at least two free memberships to give away</div>
  </div>
</div>
<div class="num" style="left:325px;top:515px">10</div>

<div class="slide" style="left:625px;top:374px">
  <div class="h abs" style="left:18px;top:14px">Engagement</div>
  <div class="abs" style="left:18px;top:26px;font-size:6px;color:#666">Major milestones about life, not just death.</div>
  <div class="photo" role="img" aria-label="Illustration of a member figure" style="left:14px;top:100px;width:24px;height:32px;background:#2a6fb0;border-radius:6px 6px 0 0"></div>
  <div class="bubble" style="left:66px;top:44px;width:46px;height:26px;background:var(--green)">Remember that guy who did the film quiz in 1990?</div>
  <div class="bubble" style="left:42px;top:78px;width:30px;height:20px;background:var(--blue)">My first day on the job</div>
  <div class="bubble" style="left:82px;top:82px;width:46px;height:28px;background:#8a8a8a">I'm working on my family history. Any old photos?</div>
  <div class="bubble" style="left:136px;top:52px;width:36px;height:24px;background:var(--blue)">Update: here's my annual holiday card</div>
  <div class="bubble" style="left:140px;top:80px;width:32px;height:24px;background:var(--green)">How would you feel about a reunion?</div>
  <div class="bubble" style="left:182px;top:42px;width:38px;height:26px;background:#8a8a8a">Was anyone else at the concert in June '77?</div>
  <div class="brand-sm"><i></i>KinThread</div>
</div>
<div class="num" style="left:625px;top:515px">11</div>

<div class="slide" style="left:925px;top:374px">
  <div class="h abs" style="left:18px;top:16px">KinThread Advantages</div>
  <div class="abs" style="left:20px;top:42px;width:12px;height:10px;border:2px solid var(--lime)"></div>
  <div class="abs body" style="left:48px;top:40px;width:150px;color:var(--muted);font-size:4.6px">Replacing paper lists, or a jumble of records and data, KinThread is a two-way channel to and from friends and relatives.</div>
  <div class="abs" style="left:20px;top:74px;width:12px;height:10px;background:var(--blue);border-radius:1px"></div>
  <div class="abs body" style="left:48px;top:72px;width:150px;color:var(--muted);font-size:4.6px">Associated services – condolence cards, flowers, e-memorials, eulogies, virtual wakes and more.</div>
  <div class="brand-sm"><i></i>KinThread</div>
</div>
<div class="num" style="left:925px;top:515px">12</div>

<!-- Row 4 -->
<div class="slide dark" style="left:25px;top:538px">
  <div class="h-white abs" style="left:18px;top:16px">Keeping Ahead of Competitors</div>
  <div class="lbox" style="left:18px;top:78px;width:62px;height:34px;background:var(--green)">First mover advantage, fast viral growth and lifetime memberships = we own the market</div>
  <div class="lbox" style="left:90px;top:58px;width:62px;height:34px;background:var(--blue)">Regular new feature releases make it difficult for competitors to plan a response</div>
  <div class="lbox" style="left:162px;top:34px;width:62px;height:34px;background:var(--lime)">Potential competitors more likely to become potential purchasers</div>
</div>
<div class="num" style="left:25px;top:679px">13</div>

<div class="slide" style="left:325px;top:538px">
  <div class="h abs" style="left:18px;top:14px">Experienced Leadership</div>
  <div class="abs" style="left:18px;top:34px;width:100px;height:28px;background:var(--green)"></div>
  <div class="photo" role="img" aria-label="Portrait photo of Paul Neville" style="left:20px;top:36px;width:22px;height:24px;background:#9a9a9a"></div>
  <div class="abs" style="left:45px;top:37px;color:#fff;font-size:3.8px;line-height:1.25;width:70px"><b>Paul Neville, Director</b><br><i>Founder of a software studio, early web products pioneer</i></div>
  <div class="abs" style="left:126px;top:34px;width:100px;height:28px;background:var(--blue)"></div>
  <div class="photo" role="img" aria-label="Portrait photo of Daniel Marsh" style="left:128px;top:36px;width:22px;height:24px;background:#a5a5a5"></div>
  <div class="abs" style="left:153px;top:37px;color:#fff;font-size:3.8px;line-height:1.25;width:70px"><b>Daniel Marsh,<br>CEO &amp; Founder</b><br><i>Internet publisher, travel and technology writer</i></div>
  <div class="abs" style="left:18px;top:70px;width:100px;height:28px;background:var(--blue)"></div>
  <div class="photo" role="img" aria-label="Portrait photo of Frank Hollis" style="left:20px;top:72px;width:22px;height:24px;background:#9a9a9a"></div>
  <div class="abs" style="left:45px;top:73px;color:#fff;font-size:3.8px;line-height:1.25;width:70px"><b>Frank Hollis, Senior VP</b><br><i>International communications advisor, management consultant</i></div>
  <div class="abs" style="left:126px;top:70px;width:100px;height:28px;background:var(--green)"></div>
  <div class="photo" role="img" aria-label="Portrait photo of Jake Dawson" style="left:128px;top:72px;width:22px;height:24px;background:#a5a5a5"></div>
  <div class="abs" style="left:153px;top:73px;color:#fff;font-size:3.8px;line-height:1.25;width:70px"><b>Jake Dawson,<br>Tech VP</b><br><i>Web and app architect, database lead</i></div>
  <div class="brand-sm" style="right:100px"><i></i>KinThread</div>
</div>
<div class="num" style="left:325px;top:679px">14</div>

<div class="slide" style="left:625px;top:538px">
  <div class="h abs" style="left:18px;top:14px">Quickly Profitable</div>
  <div class="box" style="left:20px;top:32px;width:204px;background:var(--blue)">Freemium model = 95% of memberships will be free</div>
  <div class="box" style="left:20px;top:50px;width:204px;background:var(--lime)">5% paying memberships plus<br>ongoing monetization of all members = substantial revenue</div>
  <div class="box" style="left:20px;top:74px;width:204px;background:var(--teal-dark)">Viral growth = minimal marketing costs</div>
  <div class="box" style="left:20px;top:92px;width:204px;background:var(--green)">Low costs = high profits</div>
  <div class="brand-sm"><i></i>KinThread</div>
</div>
<div class="num" style="left:625px;top:679px">15</div>

<div class="slide dark" style="left:925px;top:538px">
  <div class="h-white abs" style="left:18px;top:16px">Seed Round Funding</div>
  <div class="lbox" style="left:18px;top:34px;width:62px;height:60px;background:var(--green)">Currently <b>three months</b> into nine month development and testing</div>
  <div class="lbox" style="left:88px;top:34px;width:62px;height:60px;background:var(--blue)"><b>$200,000 budget</b> for product development and beta testing</div>
  <div class="lbox" style="left:158px;top:34px;width:66px;height:60px;background:var(--lime)">Minimum buy-in<br><b>$10,000</b> (0.25%)<br><span style="font-size:3.4px">ie 5,000 preference shares @ $2</span></div>
</div>
<div class="num" style="left:925px;top:679px">16</div>

<!-- Row 5 -->
<div class="slide dark" style="left:25px;top:702px">
  <div class="h-white abs" style="left:18px;top:16px">Seed Round Funding</div>
  <div class="lbox" style="left:18px;top:34px;width:62px;height:64px;background:var(--green)">Subsequent <b>$1.5 million 'A round'</b> financing for full product launch</div>
  <div class="lbox" style="left:88px;top:34px;width:62px;height:64px;background:var(--blue)">'A round' funding planned at <b>$5/share</b> and without diluting seed round shareholdings</div>
  <div class="lbox" style="left:158px;top:34px;width:66px;height:64px;background:var(--lime)">Investment is of course risky, but upside could see 87-fold return to seed investors within 3 - 4 years<br><br><span style="font-size:3.4px">ie $20,000 now = $1.75 million then</span></div>
</div>
<div class="num" style="left:25px;top:843px">17</div>

<div class="slide" style="left:325px;top:702px">
  <div class="h abs" style="left:18px;top:14px">Financial Projection</div>
  <table class="fin">
    <tr><th style="background:none"></th><th>Low Viral Growth</th><th style="background:var(--green)">High Viral Growth</th></tr>
    <tr><td>Months from A Round to break-even</td><td>Thirteen</td><td>Seven</td></tr>
    <tr><td>Cash burn to break-even</td><td>$1.7 million</td><td>$1.0 million</td></tr>
    <tr><td>First year profit after break-even</td><td>$1.2 million</td><td>$28 million</td></tr>
    <tr><td>Members at end of first year</td><td>4 million members</td><td>24 million members</td></tr>
    <tr><td>Second year profit</td><td>$3.9 million</td><td>~ $675 million</td></tr>
    <tr><td>Members at end of second year</td><td>7 million members</td><td>~ 357 million members</td></tr>
  </table>
  <div class="brand-sm"><i></i>KinThread</div>
</div>
<div class="num" style="left:325px;top:843px">18</div>

<div class="slide dark" style="left:625px;top:702px">
  <div class="h-white abs" style="left:18px;top:14px">Future Company Valuation</div>
  <div class="box" style="left:18px;top:30px;width:134px;background:var(--green);font-size:4.6px">Many social media companies are being valued at around <b>$50/active member</b></div>
  <svg class="abs" style="left:18px;top:52px" width="134" height="20" viewBox="0 0 134 20" aria-hidden="true">
    <path d="M29 0h8v9h5l-9 10-9-10h5z" fill="#fff"/>
    <path d="M96 0h8v9h5l-9 10-9-10h5z" fill="#fff"/>
  </svg>
  <div class="box" style="left:18px;top:73px;width:58px;height:44px;background:var(--blue);font-size:4.6px;padding-top:8px">7 million members suggests <b>$350 million valuation</b></div>
  <div class="box" style="left:88px;top:73px;width:64px;height:44px;background:var(--lime);font-size:4.6px;padding-top:14px"><b>IPO or buyout possibilities</b></div>
  <div class="photo" role="img" aria-label="Illustration of a crowd of member figures" style="left:168px;top:0;width:76px;height:138px;background:linear-gradient(160deg,#dfe9f2,#9fbfd8 55%,#a9c98a)"></div>
</div>
<div class="num" style="left:625px;top:843px">19</div>

<div class="slide dark" style="left:925px;top:702px">
  <div class="abs" style="left:18px;top:32px;color:var(--green);font-size:14px;font-weight:700">For more information</div>
  <div class="abs" style="left:18px;top:56px;font-size:5px">Please contact Daniel R Marsh, CEO</div>
  <div class="abs" style="left:18px;top:74px;font-size:5px;line-height:1.4">KinThread, Inc.<br>4410 Harbor View Ln<br>Lakemont, WA 98000<br>(555) 014-2290<br>Daniel@KinThreadHub.com</div>
</div>
<div class="num" style="left:925px;top:843px">20</div>

</body>
</html>
```